Seminar Workbook Template

My first project is a Workbook Template. There is a sample attached to give you an idea of the layout I like. I have added notes, in blue, to show what I want. I do want a header that will brand the workbook (should have the logo). We are looking for someone that we can continue to work 1 -1 with other, collateral projects. We want a constant look and feel and we have two projects ready to go.

Target Market(s)

My clients are Office Managers and CPAs so I want the workbook to have a professional layout and match the look and feel of my website: LedgerVineworks.com

Requirements
Must have
• Must match the feel of the Website. Must be in Word .doc format.
Should not have
• No red.

```html
<!DOCTYPE html>
<html lang="en">
<head>
<meta charset="utf-8">
<title>Ledger Vineworks – Folder Spread</title>
<link href="https://fonts.googleapis.com/css2?family=Montserrat:wght@500;600&family=Open+Sans:wght@400;600&display=swap" rel="stylesheet">
<style>
  :root {
    --bg: #cfcfcf;
    --green: #38a77a;
    --ink: #222222;
    --white: #ffffff;
    --panel: #e9e9e9;
    --text: #2b2b2b;
    --vine-top: #c9d3d2;
    --vine-mid: #7ea35a;
    --vine-low: #3f7a2c;
  }
  * { box-sizing: border-box; margin: 0; padding: 0; }
  html, body { width: 1200px; height: 800px; overflow: hidden; }
  body { background: var(--bg); font-family: "Open Sans", Arial, sans-serif; position: relative; }

  .spread {
    position: absolute; left: 40px; top: 30px; width: 1120px; height: 740px;
    display: flex; box-shadow: 0 6px 18px rgba(0,0,0,.18);
  }
  .page { position: relative; width: 560px; height: 740px; overflow: hidden; }
  .page--left { background: var(--white); }
  .page--right { background: var(--panel); }

  .band-green { position: absolute; left: 0; top: 0; width: 100%; background: var(--green); }
  .page--left .band-green { height: 340px; }
  .page--right .band-green { height: 165px; }

  .vineyard-photo {
    position: absolute;
    background: linear-gradient(180deg, var(--vine-top) 0%, var(--vine-top) 22%, var(--vine-mid) 48%, var(--vine-low) 100%);
  }
  .page--left .vineyard-photo { left: 185px; top: 340px; width: 375px; height: 200px;
    background: linear-gradient(180deg, #a9b7a9 0%, var(--vine-mid) 35%, var(--vine-low) 100%); }
  .page--right .vineyard-photo { left: 0; top: 165px; width: 560px; height: 235px; }

  .brand-box {
    position: absolute; left: 0; top: 340px; width: 185px; height: 200px;
    background: var(--ink); display: flex; align-items: center; gap: 10px; padding: 0 14px;
  }
  .brand-dot { width: 34px; height: 34px; border-radius: 50%; background: #6c8f82; flex: none; }
  .brand-text { color: var(--white); font-size: 11.5px; line-height: 1.55; }

  .client-list {
    position: absolute; left: 30px; right: 30px; top: 580px;
    display: flex; flex-wrap: wrap; justify-content: center; gap: 14px 22px;
  }
  .client-name { font-size: 12px; font-weight: 600; color: var(--text); letter-spacing: .04em; }

  .headline {
    position: absolute; top: 62px; left: 140px; width: 300px; text-align: center;
    font-family: "Montserrat", Arial, sans-serif; font-weight: 600; color: var(--white);
    font-size: 22px; line-height: 1.3; letter-spacing: .03em;
  }
  .headline-rule { display: block; width: 90px; height: 2px; background: var(--white); margin: 6px auto 0; }

  .intro {
    position: absolute; left: 70px; top: 500px; width: 440px; text-align: center;
    font-size: 12.5px; line-height: 1.6; color: var(--text);
  }
</style>
</head>
<body>
  <main class="spread">
    <section class="page page--left">
      <div class="band-green"></div>
      <div class="brand-box">
        <span class="brand-dot"></span>
        <p class="brand-text">Ledger Vineworks<br>707-555-0148</p>
      </div>
      <div class="vineyard-photo" role="img" aria-label="Photograph of hillside vineyard rows under morning fog"></div>
      <div class="client-list">
        <span class="client-name">Brambleton Vineyards</span>
        <span class="client-name">Ferro</span>
        <span class="client-name">Kestrel</span>
        <span class="client-name">Talon Oak Winery</span>
        <span class="client-name">Heronwood</span>
        <span class="client-name">Larkspur</span>
        <span class="client-name">Mule &amp; Kid</span>
        <span class="client-name">Morrow Wine Co.</span>
        <span class="client-name">Halvorsen</span>
        <span class="client-name">Terra Alta</span>
        <span class="client-name">Whitestone Cellars</span>
        <span class="client-name">Cobbleford Wines</span>
        <span class="client-name">Wayfarer Cellars</span>
      </div>
    </section>

    <section class="page page--right">
      <div class="band-green"></div>
      <h1 class="headline">YOUR WINERY<br>ACCOUNTING EXPERT<span class="headline-rule"></span></h1>
      <div class="vineyard-photo" role="img" aria-label="Photograph of terraced vineyard slopes with evergreen trees and fog"></div>
      <p class="intro">We are the small winery expert. Training owners and office managers of small wineries using LedgerBooks is all we do. You will be more confident, have more clarity, and be more efficient with a single online course or a full membership in our winery management club.</p>
    </section>
  </main>
</body>
</html>
```